Design new marketing postcard for mortgage loan applicants

I have provided a postcard recently designed as a possible guide for this project and have attached it. The new text is rough drafted and included. Please feel free to design outside of the old postcard or you can design close to it.

```html
<!DOCTYPE html>
<html lang="en">
<head>
<meta charset="utf-8">
<title>Cash Out Equity Loan Postcard</title>
<link href="https://fonts.googleapis.com/css2?family=Oswald:wght@600;700&family=Lato:ital,wght@0,400;0,700;0,900;1,400&display=swap" rel="stylesheet">
<style>
  :root{
    --backdrop:#3a3a3a;
    --card:#ffffff;
    --navy:#0f2540;
    --red:#e8262a;
    --gold:#e6a84c;
    --gold-light:#f6d08e;
    --ink:#2b2f36;
    --muted:#3b4350;
  }
  *{margin:0;padding:0;box-sizing:border-box}
  html,body{width:1200px;height:1200px;overflow:hidden;background:var(--backdrop)}
  body{position:relative;font-family:"Lato",sans-serif;color:var(--ink)}
  .board{position:absolute;inset:10px;border:1px solid #5a5a5a;background:radial-gradient(circle at 50% 45%,#4a4a4a,#333 80%)}
  .card{position:absolute;background:var(--card);overflow:hidden;box-shadow:0 6px 18px rgba(0,0,0,.45)}
  .card--front{left:205px;top:38px;width:780px;height:551px}
  .card--back{left:203px;top:615px;width:784px;height:554px}
  .card svg.shapes{position:absolute;inset:0;width:100%;height:100%}
  .abs{position:absolute}
  .headline{font-family:"Oswald",sans-serif;font-weight:700;color:var(--red);line-height:1;white-space:nowrap}
  .headline--main{left:18px;top:13px;font-size:83px;letter-spacing:1px}
  .headline--sub{left:19px;top:96px;font-size:61px}
  .tagline{left:15px;top:162px;width:340px;height:34px;background:var(--navy);color:var(--gold-light);font-size:23px;padding-left:10px;line-height:34px;white-space:nowrap}
  .benefits{left:22px;top:206px;list-style:none;font-size:19.5px;color:var(--muted)}
  .benefits li{display:flex;align-items:center;height:31.8px}
  .benefits svg{width:17px;height:17px;margin-right:9px}
  .brand{display:flex;align-items:center;gap:8px}
  .brand__mark{width:24px;height:24px;border-radius:50%;background:var(--gold)}
  .brand__name{font-family:"Lato",sans-serif;font-weight:700;color:var(--navy);font-size:15px;line-height:1.1}
  .front-brand{left:20px;top:385px}
  .nmls{left:213px;top:390px;font-size:19px;font-weight:700;color:var(--navy);border-left:2px solid var(--navy);padding-left:8px;line-height:24px}
  .nmls span{color:var(--gold)}
  .call{display:flex;align-items:center}
  .call__badge{position:relative;background:var(--red);color:#fff;font-weight:900;font-size:36px;border-radius:6px;height:56px;padding:0 12px;line-height:56px}
  .call__badge::after{content:"";position:absolute;right:-7px;top:21px;border-left:8px solid var(--red);border-top:7px solid transparent;border-bottom:7px solid transparent}
  .call__number{font-weight:900;color:#fff;font-size:70px;margin-left:14px;letter-spacing:-1px;text-shadow:0 2px 3px rgba(0,0,0,.45)}
  .front-call{left:129px;top:476px}
  .back-brand{left:62px;top:52px}
  .back-brand .brand__name{font-size:16px}
  .message{left:20px;top:125px;width:322px;font-size:13.8px;line-height:20.6px;color:var(--ink)}
  .quote{left:28px;top:236px;color:#fff;font-size:18.5px;line-height:21px}
  .quote span{color:var(--gold)}
  .fineprint{left:20px;top:306px;width:372px;font-style:italic;font-size:10.4px;line-height:16.8px;color:var(--muted)}
  .back-call{left:155px;top:482px}
</style>
</head>
<body>
<div class="board"></div>

<section class="card card--front">
  <svg class="shapes" viewBox="0 0 780 551">
    <defs>
      <linearGradient id="photoTone" x1="0" y1="0" x2="1" y2="1">
        <stop offset="0" stop-color="#8fa3b3"/>
        <stop offset=".45" stop-color="#d9a98a"/>
        <stop offset="1" stop-color="#efe7dc"/>
      </linearGradient>
      <linearGradient id="goldFade" x1="0" y1="0" x2="1" y2="0">
        <stop offset="0" stop-color="#e6a84c" stop-opacity="0"/>
        <stop offset=".5" stop-color="#e6a84c"/>
        <stop offset="1" stop-color="#f6d08e"/>
      </linearGradient>
      <linearGradient id="paper" x1="0" y1="0" x2="1" y2="1">
        <stop offset="0" stop-color="#ffffff"/>
        <stop offset="1" stop-color="#e9ecef"/>
      </linearGradient>
    </defs>
    <rect width="780" height="551" fill="url(#paper)"/>
    <polygon points="395,0 780,0 780,412 540,386" fill="url(#photoTone)" role="img" aria-label="Photo of a smiling couple in front of their house"/>
    <polygon points="374,0 395,0 540,386 527,386" fill="#e6a84c"/>
    <polygon points="250,448 671,345 780,398 780,412 671,368 0,490 0,488" fill="url(#goldFade)"/>
    <polygon points="0,490 671,368 780,412 780,551 0,551" fill="var(--navy)"/>
  </svg>

  <h1 class="abs headline headline--main">CASH OUT</h1>
  <p class="abs headline headline--sub">EQULITY LOAN</p>
  <p class="abs tagline">On your invesment Property</p>
  <ul class="abs benefits">
    <li><svg viewBox="0 0 17 17"><rect x="1" y="2" width="13" height="13" fill="none" stroke="#3b4350" stroke-width="1.6"/><path d="M4 8l3 3 8-9" fill="none" stroke="#3b4350" stroke-width="1.8"/></svg>Loan Based on your equily</li>
    <li><svg viewBox="0 0 17 17"><rect x="1" y="2" width="13" height="13" fill="none" stroke="#3b4350" stroke-width="1.6"/><path d="M4 8l3 3 8-9" fill="none" stroke="#3b4350" stroke-width="1.8"/></svg>Fast Close</li>
    <li><svg viewBox="0 0 17 17"><rect x="1" y="2" width="13" height="13" fill="none" stroke="#3b4350" stroke-width="1.6"/><path d="M4 8l3 3 8-9" fill="none" stroke="#3b4350" stroke-width="1.8"/></svg>No income Qualitying</li>
    <li><svg viewBox="0 0 17 17"><rect x="1" y="2" width="13" height="13" fill="none" stroke="#3b4350" stroke-width="1.6"/><path d="M4 8l3 3 8-9" fill="none" stroke="#3b4350" stroke-width="1.8"/></svg>Not based on credit Scores</li>
    <li><svg viewBox="0 0 17 17"><rect x="1" y="2" width="13" height="13" fill="none" stroke="#3b4350" stroke-width="1.6"/><path d="M4 8l3 3 8-9" fill="none" stroke="#3b4350" stroke-width="1.8"/></svg>Competitive Rates</li>
  </ul>
  <div class="abs brand front-brand"><span class="brand__mark"></span><span class="brand__name">Summit Harbor<br>Lending, Inc.</span></div>
  <p class="abs nmls">NMLS <span>#418273</span></p>
  <div class="abs call front-call"><span class="call__badge">CALL</span><span class="call__number">800-555-0147</span></div>
</section>

<section class="card card--back">
  <svg class="shapes" viewBox="0 0 784 554">
    <defs>
      <linearGradient id="goldFadeBack" x1="0" y1="0" x2="1" y2="0">
        <stop offset="0" stop-color="#e6a84c" stop-opacity="0"/>
        <stop offset=".5" stop-color="#e6a84c"/>
        <stop offset="1" stop-color="#f6d08e"/>
      </linearGradient>
      <linearGradient id="paperBack" x1="0" y1="0" x2="1" y2="1">
        <stop offset="0" stop-color="#ffffff"/>
        <stop offset="1" stop-color="#e9ecef"/>
      </linearGradient>
    </defs>
    <polygon points="0,0 289,0 473,413 0,473" fill="url(#paperBack)"/>
    <polygon points="289,0 308,0 486,413 473,413" fill="#e6a84c"/>
    <polygon points="0,229 389,229 411,285 0,285" fill="var(--navy)"/>
    <polygon points="200,450 705,392 784,430 784,443 705,405 0,475 0,473" fill="url(#goldFadeBack)"/>
    <polygon points="0,475 705,405 784,443 784,554 0,554" fill="var(--navy)"/>
    <rect x="679.5" y="16.5" width="88" height="87" fill="none" stroke="#9aa0a6"/>
    <g stroke="#8a8f95" stroke-width="1">
      <line x1="522" y1="250" x2="764" y2="250"/>
      <line x1="522" y1="286" x2="764" y2="286"/>
      <line x1="522" y1="320" x2="764" y2="320"/>
      <line x1="522" y1="354" x2="764" y2="354"/>
    </g>
  </svg>

  <div class="abs brand back-brand"><span class="brand__mark"></span><span class="brand__name">Summit Harbor<br>Lending, Inc.</span></div>
  <p class="abs message">I am Pleased to inform you that an equity based loan available for your investment property. this no qualifying loan is possible simple due to the equity you have.</p>
  <p class="abs quote">Please Call For a Quote<br>you can Also <span>Email :info@shl.loan</span></p>
  <p class="abs fineprint">*loan is subject to confirmation of equity is for income property, investment property, rental property business purpose, other conditions and invester apply. Please call for complete program requirements and details. Summit Harbor Lending, Inc. 220 Orchard Lane suite 4, Fairview CA 90000. CA Dept of Real Estate - Real Estate Broker Lic. # 00000000 NMLS # 000000, CA Dept. of real estate Corporation Lic #00000000, NMLS #000000</p>
  <div class="abs call back-call"><span class="call__badge">CALL</span><span class="call__number">800-555-0147</span></div>
</section>
</body>
</html>
```